Business Card Design Project

We need a business card design for an existing company in Dallas/Fort Worth that is expanding services and re-branding. We are changing the name from Brightmoor Commercial Cleaning to Keystride Facility Services. We are expanding from only commercial cleaning to include complete commercial landscape and facility maintenance services, too.

As stated, we offer a package of services that includes landscape, janitorial and facility services, which is largely unique in the industry.

We would like a design that communicates trust/partnership with a professional, corporate image, but not necessarily using the standard white business card. We would like a design that perhaps uses darker blues or perhaps a gray background, but we are open to other ideas. We might also be interested in a double-sided design - maybe with our logo on the back, printed on a gray background?

We will probably stick with the attached logo, but if you've got another inspired idea....

Target Market(s)

Property managers, commercial real estate professionals, corporate executives

Industry/Entity Type

Landscape

Requirements
Should not have
• Not interested in old style fonts.

```html
<!DOCTYPE html>
<html lang="en">
<head>
<meta charset="utf-8">
<title>Keystride Facility Services – Business Card</title>
<link rel="stylesheet" href="https://fonts.googleapis.com/css2?family=Michroma&family=Jura:wght@500;600&display=swap">
<style>
  :root {
    --card-dark-1: #1f1f1f;
    --card-dark-2: #4a4a4a;
    --band-1: #9a9a9a;
    --band-2: #f4f4f4;
    --ink-light: #ffffff;
    --ink-dark: #2b2b2b;
    --ink-mid: #555555;
    --rule: #8a8a8a;
    --tab: #2e2e2e;
  }
  * { box-sizing: border-box; margin: 0; padding: 0; }
  html, body { width: 1200px; height: 861px; overflow: hidden; }
  body {
    background: linear-gradient(180deg, #c9c9c9 0%, #ececec 100%);
    position: relative;
    font-family: "Jura", sans-serif;
  }
  .card {
    position: absolute;
    top: 280px;
    width: 520px;
    height: 300px;
    border-radius: 18px;
    overflow: hidden;
    box-shadow: 0 10px 28px rgba(0,0,0,.28);
  }

  /* Front */
  .card--front {
    left: 50px;
    background: linear-gradient(160deg, var(--card-dark-2) 0%, var(--card-dark-1) 60%, #2c2c2c 100%);
    color: var(--ink-light);
  }
  .front-identity {
    position: absolute;
    left: 0; right: 0;
    top: 82px;
    display: flex;
    flex-direction: column;
    align-items: center;
    gap: 14px;
  }
  .brand-name {
    font-family: "Michroma", sans-serif;
    font-weight: 400;
    color: currentColor;
    white-space: nowrap;
  }
  .front-identity .brand-name { font-size: 15px; letter-spacing: 1px; }
  .tagline {
    font-size: 11px;
    font-weight: 600;
    white-space: nowrap;
    color: #d8d8d8;
  }
  .front-band {
    position: absolute;
    left: 0; right: 0;
    top: 185px;
    height: 34px;
    background: linear-gradient(90deg, var(--band-1) 0%, var(--band-2) 45%, #dcdcdc 70%, var(--band-1) 100%);
    display: flex;
    align-items: center;
    justify-content: flex-end;
    padding-right: 120px;
  }
  .front-band__url {
    font-family: "Michroma", sans-serif;
    font-size: 13px;
    color: var(--ink-dark);
  }

  /* Back */
  .card--back {
    left: 630px;
    background: linear-gradient(160deg, #ffffff 0%, #f4f4f4 55%, #dcdcdc 100%);
    color: var(--ink-dark);
  }
  .name-tab {
    position: absolute;
    left: 0; top: 55px;
    width: 262px; height: 56px;
    background: linear-gradient(180deg, #4a4a4a, var(--tab));
    border-radius: 0 28px 28px 0;
    border: 2px solid #bdbdbd;
    border-left: none;
    color: var(--ink-light);
    padding: 8px 0 0 46px;
  }
  .name-tab__name { font-family: "Michroma", sans-serif; font-size: 17px; display: block; }
  .name-tab__position { font-size: 12px; font-weight: 500; display: block; margin-top: 2px; }
  .back-identity {
    position: absolute;
    right: 22px; top: 60px;
    display: flex;
    flex-direction: column;
    align-items: flex-end;
    gap: 6px;
    color: var(--ink-mid);
  }
  .back-identity .brand-name { font-size: 8.5px; letter-spacing: .5px; }
  .back-identity .tagline { font-size: 7px; color: var(--ink-mid); }
  .contact-list {
    position: absolute;
    left: 46px; top: 128px;
    list-style: none;
    font-size: 12px;
    font-weight: 600;
    color: var(--ink-dark);
  }
  .contact-list li { display: flex; align-items: center; gap: 10px; height: 18px; }
  .contact-list svg { width: 11px; height: 11px; fill: #777; flex: none; }
  .back-rule {
    position: absolute;
    left: 46px; right: 18px; top: 245px;
    border-top: 1.5px solid var(--rule);
  }
  .address {
    position: absolute;
    left: 46px; top: 258px;
    display: flex; align-items: center; gap: 8px;
    font-size: 13px; font-weight: 600;
  }
  .address svg { width: 14px; height: 18px; fill: #777; }
</style>
</head>
<body>

<section class="card card--front" aria-label="Card front">
  <div class="front-identity">
    <p class="brand-name">KEYSTRIDE FACILITY SERVICES</p>
    <p class="tagline">Grounds, Cleaning and Building Care Under One Roof</p>
  </div>
  <div class="front-band"><span class="front-band__url">www.keystridefs.com</span></div>
</section>

<section class="card card--back" aria-label="Card back">
  <div class="name-tab">
    <span class="name-tab__name">Name Surname</span>
    <span class="name-tab__position">Position</span>
  </div>
  <div class="back-identity">
    <p class="brand-name">KEYSTRIDE FACILITY SERVICES</p>
    <p class="tagline">Grounds, Cleaning and Building Care Under One Roof</p>
  </div>

  <ul class="contact-list">
    <li><svg viewBox="0 0 12 12"><path d="M2 1l2 0 1 3-1.5 1a7 7 0 0 0 3 3L7.5 6.5l3 1 0 2-1.5 1.5C5 11 1 7 .5 3z"/></svg>214.555.0148</li>
    <li><svg viewBox="0 0 12 12"><rect x="3" y="0" width="6" height="12" rx="1"/></svg>214.555.0192</li>
    <li><svg viewBox="0 0 12 12"><rect x="0" y="2" width="12" height="8"/><path d="M0 2l6 5 6-5" fill="none" stroke="#fff" stroke-width="1"/></svg>name@keystridefs.com</li>
    <li><svg viewBox="0 0 12 12"><circle cx="6" cy="6" r="5"/></svg>keystridefs.facebook</li>
    <li><svg viewBox="0 0 12 12"><circle cx="6" cy="6" r="5"/></svg>keystridefacilityservices</li>
    <li><svg viewBox="0 0 12 12"><rect x="0" y="1" width="12" height="8"/><rect x="4" y="10" width="4" height="1.5"/></svg>www.keystridefs.com</li>
  </ul>

  <div class="back-rule"></div>
  <p class="address">
    <svg viewBox="0 0 14 18"><path d="M0 4h9V0h5v18H0z"/><g fill="#fff"><rect x="2" y="6" width="2" height="2"/><rect x="5" y="6" width="2" height="2"/><rect x="2" y="10" width="2" height="2"/><rect x="5" y="10" width="2" height="2"/><rect x="10" y="3" width="2" height="2"/><rect x="10" y="7" width="2" height="2"/></g></svg>
    #123 Lorem Ipsum Street, Dolor sit City, PA 19017
  </p>
</section>

</body>
</html>
```